Redesign and move to Wordpress for quarvendo.com

Our website needs a redesign and at the same time we are moving it to Wordpress. Please help us with a new digital professional look and feel.

We are an Australian Software Engineering company specialising in advanced software development using in A.I., PLatform Engineering, Integration and Cloud. See the current quarvendo.com for more information about us.

```html
<!DOCTYPE html>
<html lang="en">
<head>
<meta charset="utf-8">
<title>Quarvendo — Reliable Smart Software Engineering</title>
<link href="https://fonts.googleapis.com/css2?family=Michroma&family=Poppins:wght@400;500;600;700&display=swap" rel="stylesheet">
<style>
:root{
  --blue:#1a63b0;
  --teal:#4cc3bb;
  --navy:#061a33;
  --navy-deep:#050f20;
  --ink:#1d1d1f;
  --muted:#666c75;
  --line:#e6e8ec;
  --white:#ffffff;
}
*{margin:0;padding:0;box-sizing:border-box}
html,body{width:1200px;height:3738px;overflow:hidden;background:var(--white)}
body{position:relative;font-family:"Poppins",sans-serif;color:var(--ink)}
.abs{position:absolute}
.display{font-family:"Michroma",sans-serif;font-weight:400;letter-spacing:1px}
.brand{display:flex;align-items:center;gap:12px;font-family:"Poppins",sans-serif;font-weight:500;font-size:30px;letter-spacing:1px}
.brand .mark{width:30px;height:30px;border:3px solid currentColor}
.btn{position:absolute;display:flex;align-items:center;justify-content:center;gap:12px;font-size:13px;font-weight:500;border:2px solid var(--teal);color:var(--teal);background:transparent}
.btn .arr{width:20px;height:15px;background:var(--teal);display:flex;align-items:center;justify-content:center}
.btn.light{border-color:var(--white);color:var(--white)}
.btn.light .arr{background:var(--white)}
.ph{position:absolute}

/* nav */
.nav a{position:absolute;top:38px;font-size:15px;color:var(--ink);text-decoration:none}
.nav a.active{color:var(--blue);font-weight:600}

/* hero */
.hero-title{position:absolute;left:113px;font-size:44px;line-height:1}
.hero-title.blue{color:var(--blue)}
.hero-title.teal{color:var(--teal)}

/* about */
.about p{font-size:17px;line-height:25px;color:var(--ink)}

/* logos */
.partner{position:absolute;top:1356px;font-size:24px;font-weight:600;color:#3a3a3a;display:flex;align-items:center;gap:8px}
.partner .sq{width:14px;height:14px;background:#3a3a3a}

/* services */
.svc-title{position:absolute;left:141px;color:var(--white);font-size:17px;font-weight:600}

/* news */
.card{position:absolute;top:2861px;width:288px;height:285px;background:var(--white);padding:20px 20px 0 20px;box-shadow:0 6px 18px rgba(0,0,0,.06)}
.card .date{font-size:11px;color:var(--muted);display:flex;align-items:center;gap:8px}
.card h3{font-size:16px;line-height:21px;font-weight:600;margin-top:12px}
.card .tags{font-size:11px;color:var(--muted);margin-top:14px;display:flex;gap:8px}
.card .tags span::before{content:"";display:inline-block;width:5px;height:5px;border-radius:50%;background:var(--teal);margin-right:3px;vertical-align:middle}
.card p{font-size:12.5px;line-height:20px;color:var(--muted);margin-top:14px}
.card .more{position:absolute;left:20px;top:244px;font-size:13px;font-weight:600}

/* footer */
.foot h4{position:absolute;color:var(--white);font-size:16px;font-weight:600}
.foot a,.foot .t{position:absolute;color:#d7dde6;font-size:13px;text-decoration:none}
</style>
</head>
<body>

<!-- header -->
<header class="abs" style="left:0;top:0;width:1200px;height:83px">
  <div class="brand abs" style="left:112px;top:26px;color:var(--blue)"><span class="mark"></span><span style="color:#2a2a2a">quarvendo</span></div>
  <nav class="nav">
    <a class="active" style="left:633px">Home</a>
    <a style="left:705px">About Us</a>
    <a style="left:800px">Services</a>
    <a style="left:890px">Blog</a>
    <a style="left:950px">Contact Us</a>
  </nav>
  <svg class="abs" style="left:1057px;top:37px" width="20" height="20" viewBox="0 0 20 20"><circle cx="8.5" cy="8.5" r="6.5" fill="none" stroke="var(--teal)" stroke-width="1.6"/><line x1="13.5" y1="13.5" x2="18" y2="18" stroke="var(--teal)" stroke-width="1.6"/></svg>
</header>

<!-- hero -->
<section class="hero">
  <div class="abs" style="left:0;top:207px;width:5px;height:244px;background:var(--blue)"></div>
  <div class="ph" role="img" aria-label="Hands typing on a laptop beneath glowing technology icons" style="left:544px;top:83px;width:656px;height:493px;background:linear-gradient(135deg,#1e3a66 0%,#0d2447 55%,#2b4f7d 100%)"></div>
  <div class="abs" style="left:856px;top:576px;width:344px;height:48px;background:var(--blue)"></div>
  <h1 class="hero-title display blue" style="top:258px">Reliable Smart</h1>
  <div class="hero-title display teal" style="top:312px">SOFTWARE</div>
  <div class="hero-title display blue" style="top:364px">ENGINEERING</div>
  <a class="btn" style="left:113px;top:440px;width:144px;height:37px">Schedule Now <span class="arr"><svg width="10" height="8" viewBox="0 0 10 8"><path d="M0 4h8M5 1l3 3-3 3" stroke="#fff" fill="none" stroke-width="1.4"/></svg></span></a>
</section>

<!-- about -->
<section class="about">
  <div class="ph" role="img" aria-label="White robot mascot" style="left:123px;top:631px;width:153px;height:225px;border-radius:45%;background:radial-gradient(circle at 50% 40%,#e9edf2 0%,#c9d0d8 60%,#ffffff 100%)"></div>
  <div class="abs" style="left:347px;top:667px;width:4px;height:141px;background:var(--blue)"></div>
  <h2 class="abs display" style="left:387px;top:662px;font-size:32px;color:#2a2a2a">About Quarvendo</h2>
  <p class="abs" style="left:386px;top:712px;width:645px">At Quarvendo, we craft bespoke software solutions that are not available on the market. By building organizations market-leading products, process automation, legacy system enablement, or advanced intelligent systems, we empower our customers to achieve a competitive edge in their industry.</p>
</section>

<!-- excited -->
<section class="excited">
  <div class="abs" style="left:225px;top:934px;width:167px;height:111px;background:var(--blue)"></div>
  <div class="ph" role="img" aria-label="Dark blue circuit board close-up" style="left:225px;top:1059px;width:167px;height:240px;background:linear-gradient(160deg,#1d3f5e,#0b1e33)"></div>
  <div class="ph" role="img" aria-label="Smiling professional working at a laptop" style="left:406px;top:934px;width:169px;height:234px;background:linear-gradient(180deg,#e7e7e5,#c7ccd2)"></div>
  <div class="ph" role="img" aria-label="Hand holding a tablet with glowing digital icons" style="left:406px;top:1184px;width:169px;height:115px;background:linear-gradient(180deg,#0f2340,#3a2d25)"></div>
  <div class="abs" style="left:154px;top:1100px;width:122px;height:122px;border-radius:50%;background:#e9ebee"></div>
  <div class="abs" style="left:173px;top:1119px;width:84px;height:84px;border-radius:50%;background:#8a8f96;color:#fff;text-align:center;font-size:10px;line-height:13px;padding-top:20px">★★★★★<br>Trusted By<br>People</div>
  <h2 class="abs display" style="left:652px;top:990px;font-size:28px;line-height:34px;color:#2a2a2a">EXCITED ABOUT<br>SOFTWARE<br>ENGINEERING</h2>
  <p class="abs" style="left:652px;top:1100px;width:320px;font-size:14px;line-height:20px">We have been on a mission to make complex custom enterprise integration accessible to any organisation, regardless of industry, size, or location.</p>
  <a class="btn" style="left:652px;top:1210px;width:117px;height:38px">Read More <span class="arr"><svg width="10" height="8" viewBox="0 0 10 8"><path d="M0 4h8M5 1l3 3-3 3" stroke="#fff" fill="none" stroke-width="1.4"/></svg></span></a>
</section>

<!-- partners -->
<section class="partners">
  <div class="partner" style="left:232px">Norvale</div>
  <div class="partner" style="left:414px">Tranmark</div>
  <div class="partner" style="left:610px;font-size:18px"><span class="sq"></span>Kestrel Systems</div>
  <div class="partner" style="left:823px;font-weight:500">Brightfund</div>
</section>

<!-- cta project -->
<section class="project">
  <div class="abs" style="left:225px;top:1518px;width:975px;height:258px;background:var(--teal)"></div>
  <div class="ph" role="img" aria-label="Silver humanoid robot in a thinking pose" style="left:929px;top:1400px;width:271px;height:376px;border-radius:40% 40% 0 0;background:linear-gradient(180deg,#d9dde2,#7d858f)"></div>
  <h2 class="abs display" style="left:273px;top:1565px;font-size:27px;line-height:36px;color:var(--white)">Let's start a cool project<br>with Quarvendo</h2>
  <p class="abs" style="left:277px;top:1645px;font-size:13px;color:var(--white)">We Provide Best Solution For Your Business</p>
  <a class="btn light" style="left:274px;top:1690px;width:144px;height:40px">Start a Project <span class="arr"><svg width="10" height="8" viewBox="0 0 10 8"><path d="M0 4h8M5 1l3 3-3 3" stroke="var(--teal)" fill="none" stroke-width="1.4"/></svg></span></a>
</section>

<!-- services -->
<section class="services">
  <div class="abs" style="left:0;top:1776px;width:1200px;height:691px;background:linear-gradient(120deg,#0d2c52 0%,var(--navy) 45%,var(--navy-deep) 100%)"></div>
  <div class="abs" style="left:113px;top:1843px;width:245px;height:268px;background:var(--blue);border-top:3px solid var(--teal);border-right:3px solid var(--teal)"></div>
  <svg class="abs" style="left:141px;top:1864px" width="50" height="46" viewBox="0 0 50 46" fill="none" stroke="#fff" stroke-width="1.5"><circle cx="5" cy="5" r="4"/><circle cx="25" cy="5" r="4"/><circle cx="45" cy="5" r="4"/><circle cx="5" cy="23" r="4"/><circle cx="25" cy="23" r="4"/><circle cx="45" cy="23" r="4"/><circle cx="5" cy="41" r="4"/><circle cx="25" cy="41" r="4"/><circle cx="45" cy="41" r="4"/><path d="M9 23h12M29 23h12M25 27v10"/></svg>
  <div class="svc-title" style="top:1926px;line-height:22px">Enterprise systems<br>integration</div>
  <p class="abs" style="left:141px;top:1982px;width:200px;font-size:12px;line-height:17.5px;color:#d7e3f3">Automate your business processes internally or externally to improve data quality and process efficiency</p>
  <div class="abs" style="left:141px;top:2067px;font-size:13px;font-weight:600;color:#fff">Read More &nbsp;→</div>

  <div class="ph" role="img" aria-label="Glowing grid of microchip blocks" style="left:377px;top:1901px;width:247px;height:244px;background:linear-gradient(160deg,#1f4a7a,#0c1d33 60%,#6b4a16)"></div>
  <div class="svc-title" style="left:403px;top:2090px">Microservices</div>

  <div class="ph" role="img" aria-label="Finger touching glowing hexagon icons" style="left:113px;top:2129px;width:245px;height:243px;background:linear-gradient(140deg,#14345a,#0c4d7a 60%,#1a7fa8)"></div>
  <div class="svc-title" style="top:2293px;line-height:22px">Platform<br>Engineering</div>

  <div class="ph" role="img" aria-label="Hand reaching toward a chatbot icon" style="left:377px;top:2162px;width:247px;height:244px;background:linear-gradient(180deg,#0a1a30,#1a3350)"></div>
  <div class="svc-title" style="left:403px;top:2347px">Conversational AI</div>

  <h2 class="abs display" style="left:682px;top:2038px;font-size:31px;color:var(--white)">Our Services</h2>
  <p class="abs" style="left:682px;top:2086px;width:320px;font-size:13.5px;line-height:20px;color:#dbe3ee">Lorem Ipsum is simply dummy text of the printing and typesetting industry. Lorem Ipsum has been the industry's standard dummy text ever since the 1500s</p>
  <a class="btn light" style="left:682px;top:2210px;width:167px;height:40px">View All Services <span class="arr"><svg width="10" height="8" viewBox="0 0 10 8"><path d="M0 4h8M5 1l3 3-3 3" stroke="var(--navy)" fill="none" stroke-width="1.4"/></svg></span></a>
</section>

<!-- news -->
<section class="news">
  <div class="abs" style="left:0;top:2902px;width:1200px;height:254px;background:var(--teal)"></div>
  <div class="abs" style="left:0;top:3156px;width:975px;height:181px;background:var(--teal)"></div>
  <h2 class="abs display" style="left:122px;top:2527px;font-size:30px;color:#2a2a2a">News &amp; articles</h2>
  <p class="abs" style="left:122px;top:2574px;font-size:13px">Updates from our industry</p>
  <a class="btn" style="left:958px;top:2542px;width:123px;height:38px">View More <span class="arr"><svg width="10" height="8" viewBox="0 0 10 8"><path d="M0 4h8M5 1l3 3-3 3" stroke="#fff" fill="none" stroke-width="1.4"/></svg></span></a>

  <div class="ph" role="img" aria-label="Rows of green-lit server racks" style="left:122px;top:2628px;width:305px;height:233px;background:linear-gradient(180deg,#1b2a2c,#3b7a2a 50%,#0c1a22)"></div>
  <div class="ph" role="img" aria-label="Team presenting an integration diagram on a whiteboard" style="left:447px;top:2628px;width:305px;height:233px;background:linear-gradient(180deg,#e4e6ea,#9aa2ad)"></div>
  <div class="ph" role="img" aria-label="Golden glowing data visualisation interface" style="left:782px;top:2628px;width:305px;height:233px;background:linear-gradient(160deg,#b9a57a,#3c3a3a 60%,#9a7a3e)"></div>

  <article class="card" style="left:139px">
    <div class="date"><svg width="12" height="12" viewBox="0 0 12 12" fill="none" stroke="#888" stroke-width="1"><rect x="1" y="2" width="10" height="9"/><path d="M1 5h10M4 1v2M8 1v2"/></svg>June 24, 2024</div>
    <h3>Why most upgrade paths for FlowLink lead to using..</h3>
    <div class="tags"><span>Integration</span><span>FlowLink</span></div>
    <p>Introduction In today's fast-evolving technological landscape, businesses are increasingly seeking r...</p>
    <div class="more">Read More &nbsp;→</div>
  </article>
  <article class="card" style="left:464px">
    <div class="date"><svg width="12" height="12" viewBox="0 0 12 12" fill="none" stroke="#888" stroke-width="1"><rect x="1" y="2" width="10" height="9"/><path d="M1 5h10M4 1v2M8 1v2"/></svg>June 24, 2024</div>
    <h3>Meet Quarvendo: The FlowLink Experts</h3>
    <div class="tags"><span>Integration</span><span>FlowLink</span><span>Kestrel</span></div>
    <p>At Quarvendo, we pride ourselves on having a team of exceptional talent, and at the height of that t...</p>
    <div class="more">Read More &nbsp;→</div>
  </article>
  <article class="card" style="left:799px">
    <div class="date"><svg width="12" height="12" viewBox="0 0 12 12" fill="none" stroke="#888" stroke-width="1"><rect x="1" y="2" width="10" height="9"/><path d="M1 5h10M4 1v2M8 1v2"/></svg>June 24, 2024</div>
    <h3>How to get visibility into your FlowLink environment</h3>
    <div class="tags"><span>Integration</span><span>FlowLink</span><span>Business Insights</span></div>
    <p>In today's fast-paced business environment, the ability to monitor and understand the flow of data w...</p>
    <div class="more">Read More &nbsp;→</div>
  </article>

  <h2 class="abs" style="left:113px;top:3208px;font-size:29px;line-height:44px;font-weight:600;color:var(--white)">Book an obligation free consultation<br>with our Lead Technologist</h2>
  <a class="btn light" style="left:701px;top:3239px;width:144px;height:38px">Schedule Now <span class="arr"><svg width="10" height="8" viewBox="0 0 10 8"><path d="M0 4h8M5 1l3 3-3 3" stroke="var(--teal)" fill="none" stroke-width="1.4"/></svg></span></a>
</section>

<!-- footer -->
<footer class="foot">
  <div class="abs" style="left:0;top:3337px;width:1200px;height:401px;background:linear-gradient(135deg,#0a2444,var(--navy-deep))"></div>
  <div class="ph" role="img" aria-label="Small robot sitting with a laptop" style="left:929px;top:3178px;width:203px;height:188px;border-radius:45%;background:radial-gradient(circle at 45% 40%,#f2f4f6,#aeb6c0)"></div>
  <div class="brand abs" style="left:116px;top:3432px;color:#fff"><span class="mark"></span><span>quarvendo</span></div>
  <div class="abs" style="left:118px;top:3515px;width:18px;height:18px;border-radius:50%;background:#c9d2de" role="img" aria-label="Social profile"></div>
  <div class="abs" style="left:154px;top:3515px;width:18px;height:18px;border-radius:50%;background:#c9d2de" role="img" aria-label="Social profile"></div>
  <div class="abs" style="left:192px;top:3515px;width:18px;height:18px;border-radius:50%;background:#c9d2de" role="img" aria-label="Social profile"></div>

  <h4 style="left:424px;top:3428px">Quick Links</h4>
  <a style="left:424px;top:3473px">Home</a>
  <a style="left:424px;top:3506px">Services</a>
  <a style="left:424px;top:3539px">About Us</a>
  <a style="left:424px;top:3572px">Blogs</a>
  <a style="left:424px;top:3604px">Contact Us</a>

  <h4 style="left:633px;top:3425px">Contact Info</h4>
  <svg class="abs" style="left:633px;top:3471px" width="14" height="14" viewBox="0 0 14 14"><path d="M3 1l3 3-2 2a8 8 0 004 4l2-2 3 3-2 2C6 13 1 8 1 3z" fill="var(--blue)"/></svg>
  <div class="t" style="left:656px;top:3470px;font-weight:600;color:#fff">Phone</div>
  <div class="t" style="left:633px;top:3488px">1800 555 019</div>
  <svg class="abs" style="left:633px;top:3518px" width="15" height="11" viewBox="0 0 15 11"><rect width="15" height="11" fill="var(--blue)"/><path d="M0 0l7.5 6L15 0" stroke="#fff" fill="none"/></svg>
  <div class="t" style="left:656px;top:3515px;font-weight:600;color:#fff">Email</div>
  <div class="t" style="left:633px;top:3532px">hello@quarvendo.com</div>
  <svg class="abs" style="left:633px;top:3566px" width="12" height="16" viewBox="0 0 12 16"><path d="M6 0a6 6 0 016 6c0 4-6 10-6 10S0 10 0 6a6 6 0 016-6z" fill="var(--blue)"/><circle cx="6" cy="6" r="2" fill="#fff"/></svg>
  <div class="t" style="left:656px;top:3567px;font-weight:600;color:#fff">Location</div>
  <div class="t" style="left:634px;top:3584px;line-height:16px">Suite 210, 8 Harbour Lane<br>Melbourne, VIC , 3000</div>

  <h4 style="left:863px;top:3422px;line-height:24px">Australia's Largest health<br>charity implements<br>Quarvendo API Msg Bus</h4>
  <div class="t" style="left:863px;top:3514px;line-height:19px;width:230px">Register to our newsletter to find out more.</div>
  <div class="abs" style="left:863px;top:3577px;width:224px;height:40px;background:#17293f;border:1px solid #24405f"></div>
  <div class="t" style="left:885px;top:3590px;font-size:12px;color:#7e8b9c">Your Email</div>
  <svg class="abs" style="left:1047px;top:3591px" width="16" height="12" viewBox="0 0 16 12"><path d="M0 6h14M9 1l5 5-5 5" stroke="var(--teal)" fill="none" stroke-width="1.5"/></svg>

  <div class="abs" style="left:113px;top:3671px;width:974px;height:1px;background:#2a3f5a"></div>
  <div class="t" style="left:0;width:1200px;text-align:center;top:3694px;color:#fff">Copyright ©2025 Quarvendo. All Rights Reserved</div>
</footer>

</body>
</html>
```